Simple and Approachable Cover for Pet Expo Company Page

Size: 2000 x 430; looking simply for words "Dunmore HR Consulting" and email address "DunmoreHRConsulting@brelvamail.com." This is for a cover photo for a company profile page for the Hollow Oak Expo, where I am a featured speaker on Employee Communications later this month. You can incorporate the attached photo to the left of the banner ad if you wish. The mood I wish to present is approachable, positive and simple.

Target Market(s)

small pet retail business owners

Industry/Entity Type

Pet Shop

Font styles to use
Serif
Sans Serif

Requirements
Must have
• Email address clearly defined/separated. Easy to read.
Nice to have
• I like the picture that I included; subtle pet paw background is also nice
Should not have
• No paid stock images

```html
<!DOCTYPE html>
<html lang="en">
<head>
<meta charset="utf-8">
<title>Dunmore HR Consulting – Cover</title>
<link href="https://fonts.googleapis.com/css2?family=Open+Sans:wght@400;800&display=swap" rel="stylesheet">
<style>
  :root {
    --sun: #f2d27b;
    --ink: #111111;
    --brand-blue: #2b5a8a;
    --accent-brown: #c47f3a;
    --white: #ffffff;
    --photo-green: #6f8a4a;
    --photo-shade: #3e5230;
    --photo-warm: #b9a27a;
  }
  * { margin: 0; padding: 0; box-sizing: border-box; }
  html, body { width: 1200px; height: 258px; overflow: hidden; background: var(--sun); }
  .cover {
    position: relative;
    width: 1200px;
    height: 258px;
    background: var(--sun);
    font-family: "Open Sans", Arial, sans-serif;
    overflow: hidden;
  }
  .cover__photo {
    position: absolute;
    left: 0; top: 0;
    width: 400px;
    height: 258px;
    background: linear-gradient(160deg, var(--photo-shade) 0%, var(--photo-green) 45%, var(--photo-warm) 100%);
    clip-path: polygon(0 0, 324px 0, 386px 258px, 0 258px);
  }
  .cover__divider {
    position: absolute;
    left: 0; top: 0;
    width: 400px; height: 258px;
  }
  .cover__emblem {
    position: absolute;
    left: 748px;
    top: 14px;
    width: 66px;
    height: 66px;
    border-radius: 50%;
    background: var(--accent-brown);
  }
  .cover__title {
    position: absolute;
    left: 395px;
    width: 790px;
    top: 103px;
    text-align: center;
    font-weight: 800;
    font-size: 62px;
    line-height: 1;
    letter-spacing: -0.5px;
    color: var(--ink);
    white-space: nowrap;
  }
  .cover__email {
    position: absolute;
    left: 565px;
    top: 197px;
    width: 450px;
    height: 42px;
    border-radius: 6px;
    background: var(--brand-blue);
    box-shadow: 0 0 0 2px rgba(255,255,255,0.35);
    color: var(--white);
    font-size: 19px;
    font-weight: 400;
    display: flex;
    align-items: center;
    justify-content: center;
    white-space: nowrap;
  }
</style>
</head>
<body>
  <div class="cover">
    <div class="cover__photo" role="img" aria-label="Photo of the consultants sitting on grass outdoors with their two hound dogs"></div>
    <svg class="cover__divider" viewBox="0 0 400 258" aria-hidden="true">
      <line x1="324" y1="0" x2="387" y2="258" stroke="var(--brand-blue)" stroke-width="5"/>
    </svg>

    <div class="cover__emblem" role="img" aria-label="Brown paw print decoration"></div>

    <h1 class="cover__title">Dunmore HR Consulting</h1>

    <div class="cover__email">DunmoreHRConsulting@brelvamail.com</div>
  </div>
</body>
</html>
```